Faux Liquor Tax Stamp
Bramble Hollow Moonshine Faux Tax Stamp
Project: Faux Liquor Tax Stamp
Faux Liquor Tax Stamp - Beverages
Creative Brief
This is the design for a sticker that fits over the cork of a liquor bottle. These are no longer used but we would like to capture the feel of the era from which they come. 600dpi for print 125mm long and 15mm wide language: TENNESSEE MOONSHINE, possible images: whiskey barrels, mules, corn, moon, filligree color: monotones preferred like in the sample links Samples: http://www.kvopwertz.com/mzq/spirit.jpg http://2.qz.plinkpost.com/_R_JmTeb5uHn/WQ4Lp2eRHKz/BBBBBBBBRzm/K3Wo9QUvvP1/s1600/tobacco_duty_marks.jpg http://glyphocollecta.com/Engines/QT284f.jpg http://smokeloreworld.info/Eras/Eras_Duty_Marks_files/NoTitle41.jpg http://www.corvellhoardsman.com/pagemakercontent/pagemakerpictures/QX_Bvel_Seal_L.jpg
Beverages
Liquor Consumers
600dpi for print 125mm long and 15mm wide language: TENNESSEE MOONSHINE

```html
<!DOCTYPE html>
<html lang="en">
<head>
<meta charset="utf-8">
<title>Tennessee Moonshine Tax Stamp</title>
<link href="https://fonts.googleapis.com/css2?family=Cinzel:wght@400;700&family=IM+Fell+English&display=swap" rel="stylesheet">
<style>
  :root {
    --stage-center: #3a3a3a;
    --stage-edge: #050505;
    --blue-dark: #1d2f5c; --blue-mid: #4f72b5; --blue-light: #a9c2ec;
    --grey-dark: #2e2e2e; --grey-mid: #8a8a8a; --grey-light: #e2e2e2;
    --tan-dark: #3a2c1a; --tan-mid: #a88f62; --tan-light: #e4d3ac;
    --red-dark: #5a1a1c; --red-mid: #c75a5e; --red-light: #f3b9b7;
    --ink-light: #f4efe6;
  }
  * { box-sizing: border-box; margin: 0; padding: 0; }
  html, body { width: 1200px; height: 799px; overflow: hidden; }
  body {
    background: radial-gradient(ellipse at center, var(--stage-center) 0%, #161616 65%, var(--stage-edge) 100%);
    position: relative;
    font-family: "IM Fell English", serif;
  }
  .stamp {
    position: absolute; left: 38px; width: 1124px; height: 134px;
    border: 3px solid var(--dark);
    background: linear-gradient(180deg, var(--dark) 0 8px, var(--mid) 8px 16px, var(--light) 50%, var(--mid) calc(100% - 16px), var(--dark) calc(100% - 8px));
    box-shadow: 0 4px 10px rgba(0,0,0,.6);
  }
  .stamp--blue { top: 84px; --dark: var(--blue-dark); --mid: var(--blue-mid); --light: var(--blue-light); }
  .stamp--grey { top: 240px; --dark: var(--grey-dark); --mid: var(--grey-mid); --light: var(--grey-light); }
  .stamp--tan  { top: 396px; --dark: var(--tan-dark); --mid: var(--tan-mid); --light: var(--tan-light); }
  .stamp--red  { top: 552px; --dark: var(--red-dark); --mid: var(--red-mid); --light: var(--red-light); }

  .border-band {
    position: absolute; left: 0; right: 0; height: 16px;
    background: linear-gradient(180deg, var(--mid), var(--light), var(--mid));
    opacity: .75;
  }
  .border-band--top { top: 10px; }
  .border-band--bottom { bottom: 10px; }

  .emblem, .engraving {
    position: absolute; top: 30px; height: 68px;
    background: linear-gradient(180deg, var(--mid), var(--light) 50%, var(--mid));
    border-radius: 6px;
  }
  .emblem--left { left: 10px; width: 44px; }
  .emblem--right { right: 10px; width: 44px; }
  .engraving--left { left: 254px; width: 124px; }
  .engraving--right { left: 746px; width: 124px; }

  .panel {
    position: absolute; top: 20px; height: 88px; width: 172px;
    background: var(--dark);
    border: 2px solid var(--light);
    outline: 2px solid var(--dark);
    color: var(--ink-light);
    display: flex; align-items: center; justify-content: center; text-align: center;
    font-size: 15px; line-height: 1.15;
  }
  .panel--left { left: 64px; font-variant: small-caps; letter-spacing: .5px; }
  .panel--right { left: 884px; font-size: 16px; }

  .plaque {
    position: absolute; left: 392px; top: 6px; width: 340px; height: 116px;
    background: linear-gradient(180deg, var(--dark), #111 50%, var(--dark));
    border: 3px solid var(--light);
    border-radius: 40px / 58px;
    display: flex; align-items: center; justify-content: center;
  }
  .plaque__title {
    font-family: "Cinzel", serif; font-weight: 400; color: var(--ink-light);
    text-align: center; font-size: 23px; line-height: 1.15; letter-spacing: 1px;
    border-top: 1px solid var(--mid); border-bottom: 1px solid var(--mid); padding: 5px 4px;
  }
  .pearl {
    position: absolute; top: 46px; width: 20px; height: 20px; border-radius: 50%;
    background: radial-gradient(circle at 35% 35%, #fff, var(--light) 40%, var(--mid));
  }
  .pearl--left { left: 26px; }
  .pearl--right { right: 26px; }
</style>
</head>
<body>
  <section class="stamp stamp--blue">
    <div class="border-band border-band--top" role="img" aria-label="Scalloped engraved border"></div>
    <div class="border-band border-band--bottom" role="img" aria-label="Scalloped engraved border"></div>
    <div class="emblem emblem--left" role="img" aria-label="Engraved beetle ornament"></div>
    <div class="panel panel--left">Authentic<br>Tennessee<br>moonshine</div>
    <div class="engraving engraving--left" role="img" aria-label="Engraved whiskey barrel illustration"></div>
    <div class="plaque"><span class="pearl pearl--left"></span><p class="plaque__title">TENNESSEE<br>MOONSHINE</p><span class="pearl pearl--right"></span></div>
    <div class="engraving engraving--right" role="img" aria-label="Engraved whiskey barrel illustration"></div>
    <div class="panel panel--right">Hand-crafted<br>with locally<br>grown stone<br>milled corn</div>
    <div class="emblem emblem--right" role="img" aria-label="Engraved beetle ornament"></div>
  </section>

  <section class="stamp stamp--grey">
    <div class="border-band border-band--top" role="img" aria-label="Scalloped engraved border"></div>
    <div class="border-band border-band--bottom" role="img" aria-label="Scalloped engraved border"></div>
    <div class="emblem emblem--left" role="img" aria-label="Engraved beetle ornament"></div>
    <div class="panel panel--left">Authentic<br>Tennessee<br>moonshine</div>
    <div class="engraving engraving--left" role="img" aria-label="Engraved whiskey barrel illustration"></div>
    <div class="plaque"><span class="pearl pearl--left"></span><p class="plaque__title">TENNESSEE<br>MOONSHINE</p><span class="pearl pearl--right"></span></div>
    <div class="engraving engraving--right" role="img" aria-label="Engraved whiskey barrel illustration"></div>
    <div class="panel panel--right">Hand-crafted<br>with locally<br>grown stone<br>milled corn</div>
    <div class="emblem emblem--right" role="img" aria-label="Engraved beetle ornament"></div>
  </section>

  <section class="stamp stamp--tan">
    <div class="border-band border-band--top" role="img" aria-label="Scalloped engraved border"></div>
    <div class="border-band border-band--bottom" role="img" aria-label="Scalloped engraved border"></div>
    <div class="emblem emblem--left" role="img" aria-label="Engraved beetle ornament"></div>
    <div class="panel panel--left">Authentic<br>Tennessee<br>moonshine</div>
    <div class="engraving engraving--left" role="img" aria-label="Engraved whiskey barrel illustration"></div>
    <div class="plaque"><span class="pearl pearl--left"></span><p class="plaque__title">TENNESSEE<br>MOONSHINE</p><span class="pearl pearl--right"></span></div>
    <div class="engraving engraving--right" role="img" aria-label="Engraved whiskey barrel illustration"></div>
    <div class="panel panel--right">Hand-crafted<br>with locally<br>grown stone<br>milled corn</div>
    <div class="emblem emblem--right" role="img" aria-label="Engraved beetle ornament"></div>
  </section>

  <section class="stamp stamp--red">
    <div class="border-band border-band--top" role="img" aria-label="Scalloped engraved border"></div>
    <div class="border-band border-band--bottom" role="img" aria-label="Scalloped engraved border"></div>
    <div class="emblem emblem--left" role="img" aria-label="Engraved beetle ornament"></div>
    <div class="panel panel--left">Authentic<br>Tennessee<br>moonshine</div>
    <div class="engraving engraving--left" role="img" aria-label="Engraved whiskey barrel illustration"></div>
    <div class="plaque"><span class="pearl pearl--left"></span><p class="plaque__title">TENNESSEE<br>MOONSHINE</p><span class="pearl pearl--right"></span></div>
    <div class="engraving engraving--right" role="img" aria-label="Engraved whiskey barrel illustration"></div>
    <div class="panel panel--right">Hand-crafted<br>with locally<br>grown stone<br>milled corn</div>
    <div class="emblem emblem--right" role="img" aria-label="Engraved beetle ornament"></div>
  </section>
</body>
</html>
```